" Iniciamos o projeto do cliente com análise do consumo de energia elétrica, a partir disso dimensionamos o sistema utilizando a melhor solução de energia solar fotovoltaica para o cliente. Elaboramos a proposta do projeto com o orçamento e após aceite do cliente iniciamos o processo de homologação junto às concessionárias e instalação do sistema no cliente com a nossa própria equipe técnica. Também apresentamos o saving e payback do projeto. "

```html
<!DOCTYPE html>
<html lang="pt-BR">
<head>
<meta charset="UTF-8">
<title>Lumera Energia Solar — O futuro já começou</title>
<link href="https://fonts.googleapis.com/css2?family=Montserrat:wght@400;500;700;800;900&display=swap" rel="stylesheet">
<style>
  :root {
    --navy: #1b2f5c;
    --navy-deep: #14244a;
    --orange: #f39200;
    --blue: #2e62a8;
    --text: #2b3a55;
    --backdrop: #e9ebee;
    --white: #ffffff;
    --panel-dark: #24407a;
    --panel-light: #7ea3d6;
  }
  * { margin: 0; padding: 0; box-sizing: border-box; }
  html, body {
    width: 1200px; height: 1200px; overflow: hidden;
    background: var(--backdrop);
    font-family: "Montserrat", Arial, sans-serif;
  }
  .slide {
    position: absolute; left: 0; top: 265px;
    width: 1200px; height: 670px;
    background: var(--white);
    overflow: hidden;
  }
  .headline {
    position: absolute; left: 14px; top: 24px;
    font-weight: 900; font-size: 44px; line-height: 52px;
    color: var(--navy); letter-spacing: -0.5px;
    white-space: nowrap;
  }
  .headline .accent { color: var(--orange); }
  .headline-rule {
    position: absolute; left: 0; top: 188px;
    width: 500px; height: 6px; background: var(--navy);
  }
  .top-band { position: absolute; right: 0; top: 0; width: 470px; height: 122px; }
  .brand {
    position: absolute; right: 26px; top: 28px;
    display: flex; align-items: center; gap: 10px;
  }
  .brand-dot { width: 22px; height: 22px; border-radius: 50%; background: var(--blue); }
  .brand-text { display: flex; flex-direction: column; align-items: center; }
  .brand-name { font-weight: 700; font-size: 32px; color: var(--navy); line-height: 1; }
  .brand-tag { font-weight: 700; font-size: 10px; letter-spacing: 3px; color: var(--navy); margin-top: 4px; }
  .panel-photo {
    position: absolute; left: 18px; top: 272px;
    width: 445px; height: 348px;
  }
  .copy { position: absolute; left: 622px; top: 272px; width: 545px; }
  .copy-title {
    font-weight: 800; font-size: 16px; line-height: 22px;
    color: var(--navy); text-transform: uppercase;
  }
  .copy-body {
    margin-top: 28px; font-size: 15.5px; line-height: 22px; color: var(--text);
  }
  .copy-body + .copy-body { margin-top: 18px; }
  .offer { position: absolute; left: 622px; top: 572px; }
  .offer-title { font-weight: 800; font-size: 26px; color: var(--navy); line-height: 32px; }
  .offer-sub {
    font-weight: 500; font-size: 24px; color: var(--orange);
    line-height: 30px; padding-left: 118px;
  }
  .footer-band {
    position: absolute; left: 0; bottom: 0; width: 100%; height: 18px;
    background: var(--navy-deep);
  }
  .footer-band::before {
    content: ""; position: absolute; left: 0; top: -4px; width: 100%; height: 4px;
    background: var(--blue);
  }
</style>
</head>
<body>
  <main class="slide">
    <h1 class="headline">
      O <span class="accent">FUTURO JÁ</span><br>
      COMEÇOU E NÓS<br>
      VAMOS <span class="accent">TE LEVAR LÁ</span>
    </h1>
    <div class="headline-rule"></div>

    <svg class="top-band" viewBox="0 0 470 122">
      <defs>
        <linearGradient id="bandPhoto" x1="0" y1="0" x2="1" y2="1">
          <stop offset="0" stop-color="#8fb4e0"/>
          <stop offset="0.5" stop-color="#3d64a6"/>
          <stop offset="1" stop-color="#1e3a70"/>
        </linearGradient>
      </defs>
      <polygon points="40,0 470,0 470,122 0,122" fill="url(#bandPhoto)" role="img" aria-label="Fotografia de painéis solares sob céu azul"/>
      <polygon points="40,0 470,0 470,4 38,4" fill="var(--blue)"/>
      <polygon points="200,10 470,10 470,112 170,112" fill="var(--white)"/>
    </svg>
    <div class="brand">
      <span class="brand-dot"></span>
      <div class="brand-text">
        <span class="brand-name">Lumera</span>
        <span class="brand-tag">ENERGIA SOLAR</span>
      </div>
    </div>

    <svg class="panel-photo" viewBox="0 0 445 348" role="img" aria-label="Fotografia de um painel solar fotovoltaico em suporte metálico">
      <defs>
        <linearGradient id="panelPhoto" x1="0" y1="0" x2="1" y2="1">
          <stop offset="0" stop-color="var(--panel-light)"/>
          <stop offset="1" stop-color="var(--panel-dark)"/>
        </linearGradient>
      </defs>
      <rect width="445" height="348" fill="url(#panelPhoto)"/>
    </svg>

    <section class="copy">
      <h2 class="copy-title">Que tal converter o poder do sol em prosperidade<br>para seu negócio e sua família?</h2>
      <p class="copy-body">Diariamente, muita energia chega ao nosso planeta de forma gratuita e limpa. Os raios solares, além de trazerem a luz e o calor, essenciais para a vida na Terra, podem ser aproveitados para a geração de energia, tanto na forma de calor, quanto na de eletricidade.</p>
      <p class="copy-body">Essa eletricidade que vem do sol é chamada de fotovoltaica.</p>
    </section>

    <div class="offer">
      <p class="offer-title">Temos a solução sob medida</p>
      <p class="offer-sub">para sua residência ou empresa.</p>
    </div>

    <div class="footer-band"></div>
  </main>
</body>
</html>
```